Steadying Downturn Worries

I need a on page electronic flyer for this coaching program. I want a silhouette to accompany the case the copy starts with. I have the copy written but need it put together in a striking way.

Target Market(s)

towards higher net worth individuals

Industry/Entity Type

Electronic

```html
<!DOCTYPE html>
<html lang="en">
<head>
<meta charset="utf-8">
<title>Steadying Downturn Worries – Coaching Flyer</title>
<link href="https://fonts.googleapis.com/css2?family=Arimo:wght@400;700&family=Oswald:wght@500;600;700&display=swap" rel="stylesheet">
<style>
  :root {
    --stage: #e4e2df;
    --paper: #ffffff;
    --navy: #0c2a56;
    --blue: #1d5c9a;
    --blue-mid: #2a6eb0;
    --sky: #8fd0f2;
    --orange: #f7941d;
    --green: #3fae49;
    --ink-light: #ffffff;
    --ink-blue: #1c4f93;
  }
  * { box-sizing: border-box; margin: 0; padding: 0; }
  html, body { width: 1200px; height: 900px; overflow: hidden; }
  body {
    background: var(--stage);
    font-family: "Arimo", Arial, sans-serif;
    position: relative;
  }
  .flyer {
    position: absolute;
    left: 300px; top: 20px;
    width: 600px; height: 860px;
    background: var(--paper);
    overflow: hidden;
    box-shadow: 0 4px 18px rgba(0,0,0,.18);
  }
  .flyer-backdrop { position: absolute; inset: 0; }

  .tagline {
    position: absolute; right: 92px; top: 18px;
    text-align: right;
    font-family: "Oswald", "Arial Narrow", sans-serif;
    font-weight: 600; font-size: 12px; line-height: 1.2;
    letter-spacing: .4px;
    color: var(--orange);
    text-transform: uppercase;
  }

  .headline {
    position: absolute; left: 40px; right: 40px; top: 86px;
    text-align: right;
    font-family: "Oswald", "Arial Narrow", sans-serif;
    text-transform: uppercase;
    line-height: 1;
  }
  .headline .kicker { display: block; color: var(--ink-light); font-weight: 600; font-size: 22px; letter-spacing: .3px; margin-bottom: 4px; }
  .headline .line { display: block; font-weight: 700; font-size: 40px; color: var(--sky); }
  .headline .plain { color: var(--ink-light); }
  .headline .connector {
    text-transform: none; font-style: italic; color: var(--orange);
    font-weight: 600; font-size: 30px; margin-right: 4px;
  }

  .case-portrait {
    position: absolute; left: 42px; top: 206px;
    width: 188px; height: 196px;
    border: 3px solid #fff;
    background: linear-gradient(180deg, #b9d3ec 0%, #6f9fd0 100%);
  }

  .case-story {
    position: absolute; left: 248px; right: 42px; top: 206px;
    color: var(--ink-light);
    font-size: 10.5px; line-height: 1.38;
  }
  .case-story p + p { margin-top: 9px; }

  .program {
    position: absolute; left: 42px; right: 42px; top: 416px;
    color: var(--ink-light);
    font-size: 10.5px; line-height: 1.36;
  }
  .program p + p, .program .outcomes + p { margin-top: 9px; }
  .program .question { font-weight: 700; margin-top: 9px; }
  .outcomes { list-style: none; margin-top: 2px; }
  .outcomes li { display: flex; align-items: center; gap: 6px; }
  .outcomes svg { flex: none; }
  .program .closing { padding-right: 92px; }

  .brand-seal {
    position: absolute; right: 18px; top: 700px;
    width: 104px; height: 104px;
    border-radius: 50%;
    background: #fff;
    display: flex; align-items: center; justify-content: center;
    text-align: center;
    font-family: "Arimo", Arial, sans-serif;
    font-weight: 700; font-size: 15px; line-height: 1.1;
    color: var(--ink-blue);
    text-transform: uppercase;
    box-shadow: 0 2px 6px rgba(0,0,0,.2);
  }

  .author-note {
    position: absolute; left: 42px; right: 140px; top: 782px;
    color: var(--ink-blue);
    font-weight: 700; font-size: 11px; line-height: 1.38;
  }
</style>
</head>
<body>
  <article class="flyer">
    <svg class="flyer-backdrop" width="600" height="860" viewBox="0 0 600 860" aria-hidden="true">
      <defs>
        <linearGradient id="panelFill" x1="0" y1="0" x2="0" y2="1">
          <stop offset="0" stop-color="#0b2750"/>
          <stop offset=".55" stop-color="#1a4f88"/>
          <stop offset="1" stop-color="#2466a6"/>
        </linearGradient>
        <radialGradient id="panelGlow" cx=".3" cy=".55" r=".55">
          <stop offset="0" stop-color="#3b7dbf" stop-opacity=".55"/>
          <stop offset="1" stop-color="#3b7dbf" stop-opacity="0"/>
        </radialGradient>
      </defs>
      <!-- right edge bands -->
      <path d="M430 0 L600 0 L600 860 L566 860 C590 600 596 300 580 120 C570 50 520 12 430 0 Z" fill="var(--green)"/>
      <path d="M470 0 L600 0 L600 860 L586 860 C600 600 604 300 594 110 C588 50 550 12 470 0 Z" fill="var(--orange)"/>
      <!-- left edge bands -->
      <path d="M0 40 C30 160 34 520 20 860 L0 860 Z" fill="var(--orange)"/>
      <path d="M0 140 C16 260 20 560 8 860 L0 860 Z" fill="var(--green)"/>
      <!-- main panel -->
      <path d="M30 66 C200 60 420 58 574 66 C582 300 580 560 574 766 L18 766 C28 520 32 300 30 66 Z" fill="url(#panelFill)"/>
      <path d="M30 66 C200 60 420 58 574 66 C582 300 580 560 574 766 L18 766 C28 520 32 300 30 66 Z" fill="url(#panelGlow)"/>
    </svg>

    <p class="tagline">Sometimes the best financial advice<br>isn't about numbers...</p>

    <h1 class="headline">
      <span class="kicker">Steadying Downturn Worries:</span>
      <span class="line"><span class="plain">From</span> Financial Worries</span>
      <span class="line"><span class="connector">to</span>Wealth Satisfaction</span>
    </h1>

    <div class="case-portrait" role="img" aria-label="Silhouette of a man in a suit, representing the client in the case story"></div>

    <section class="case-story">
      <p>A 49 year old attorney, Steve was used to success and rising net worth. But with huge losses in the market crash, layoffs at his firm, his kids heading for college and the stagnant economy stretching ahead, his usual optimism is gone.</p>
      <p>With his anxiety growing, Steve doubts his own decision making ability. His confidence slipping, he stopped opening his financial statements and could barely speak to his financial advisor. He thought if his advisor said “hang in there” one more time, he just might blow up.</p>
      <p>Yet Steve felt too embarrassed to talk about his deep worries, even with his wife. It seemed like all he could do was pour another glass of wine and suffer in isolation.</p>
    </section>

    <section class="program">
      <p>If you’re like Steve, you’re afraid and alone with plenty of company. In a September 2009 National Counseling Council poll, 80 percent reported the economy is causing significant stress, up from 66 percent from the previous April. The Restful Nights Institute said 27 percent of people surveyed had sleeplessness because of economic anxiety.</p>
      <p class="question">How can you take control of these worries and get back to enjoying your life? In this 5 session coaching process you will:</p>
      <ul class="outcomes">
        <li><svg width="10" height="10" viewBox="0 0 10 10" aria-hidden="true"><rect x=".5" y="1.5" width="7" height="7" fill="none" stroke="#fff"/><path d="M2 5 L4 7 L9.5 .8" fill="none" stroke="#fff" stroke-width="1.4"/></svg>Learn a decision making tool to make choices that truly serve your needs</li>
        <li><svg width="10" height="10" viewBox="0 0 10 10" aria-hidden="true"><rect x=".5" y="1.5" width="7" height="7" fill="none" stroke="#fff"/><path d="M2 5 L4 7 L9.5 .8" fill="none" stroke="#fff" stroke-width="1.4"/></svg>Clarify and more fully engage with your purpose and passions</li>
        <li><svg width="10" height="10" viewBox="0 0 10 10" aria-hidden="true"><rect x=".5" y="1.5" width="7" height="7" fill="none" stroke="#fff"/><path d="M2 5 L4 7 L9.5 .8" fill="none" stroke="#fff" stroke-width="1.4"/></svg>Improve your relationship with your financial advisor</li>
        <li><svg width="10" height="10" viewBox="0 0 10 10" aria-hidden="true"><rect x=".5" y="1.5" width="7" height="7" fill="none" stroke="#fff"/><path d="M2 5 L4 7 L9.5 .8" fill="none" stroke="#fff" stroke-width="1.4"/></svg>Feel more in control and confident in your financial life</li>
      </ul>
      <p>This process guides you to step back and understand the source of your financial worry—your unique story about the meaning of money. Your money story drives your emotions and decision making—for better and worse. You’ll learn a decision making tool for more conscious, effective and satisfying financial and life decisions.</p>
      <p class="closing">You’ll also examine your core values and strengths—what really matters most to you and how you work at your best. When you use your money and your core strengths to pursue your highest aspirations, life and wealth become balanced. As you commit more fully to your mission and passions, satisfaction grows and money worries melt away.</p>
    </section>

    <div class="brand-seal">Crestline<br>Circle</div>

    <p class="author-note">Dana Merrow, Ph.D. is a psychologist with 30 years of experience treating anxiety and stress. She is co-founder and facilitator of Crestline Circle, a peer learning group for high net worth investors. For more information, call 555-013-2290. dmerrow@crestlinecircle.example</p>
  </article>
</body>
</html>
```